Harlow Stonefield Civil Construction website design

We want a Bold website to promote our Heavy Civil Construction company, We would like an organic / tangible feel to the site. The pictures will be over saturated so they pop. We need to be able to easliy upload new projects and pictures on a regular basis.
Home page will have a full screen width image, "home page image" with silhouette and logo. It will also have about us area and picture
Page 2 will be Project Gallery with pictures in project folders
Page 3 will be an employment application form and submission
Page 4 will be Contact Us
Target Market(s)
Construction indusrty
Industry/Entity Type
Contractor
Coding
Coded - Design and coding required
Number of Pages Required
4 page
Font styles to use
Other font styles liked:
- Hypatia Sans Pro Light
Look and feel

```html
<!DOCTYPE html>
<html lang="en">
<head>
<meta charset="utf-8">
<title>Harlow Stonefield Civil Construction</title>
<link rel="stylesheet" href="https://fonts.googleapis.com/css2?family=Source+Sans+3:wght@300;400;600;700&family=Montserrat:wght@700;800&display=swap">
<style>
:root{
  --blue:#3a52a8;
  --blue-deep:#2c3f8c;
  --ink:#1d1f26;
  --text:#4a4d57;
  --grey-bg:#f2f2f2;
  --line:#c9ccd3;
  --footer:#1b1c22;
  --white:#ffffff;
}
*{box-sizing:border-box;margin:0;padding:0}
html,body{width:1200px;height:3241px;overflow:hidden}
body{font-family:"Source Sans 3",sans-serif;color:var(--text);background:var(--white);position:relative}
.abs{position:absolute}
section{position:absolute;left:0;width:1200px;overflow:hidden}

/* hero */
.hero{top:0;height:620px}
.hero-photo{position:absolute;inset:0;background:linear-gradient(180deg,#3d4a63 0%,#5b6a5a 22%,#6f7a4c 45%,#8a6a45 70%,#5a4a38 100%)}
.hero-photo::after{content:"";position:absolute;inset:0;background:linear-gradient(90deg,rgba(20,25,40,.35),rgba(20,25,40,0) 60%)}
.brand{position:absolute;left:235px;top:36px;display:flex;align-items:center;gap:10px;color:var(--white)}
.brand-mark{width:30px;height:30px;background:var(--blue)}
.brand-name{font-weight:600;font-size:17px;line-height:1.05;letter-spacing:.5px;text-transform:uppercase}
.brand-name small{display:block;font-size:10.5px;letter-spacing:3px;font-weight:600}
.nav{position:absolute;top:44px;left:608px;display:flex;gap:21px;font-size:10.5px;color:var(--white);letter-spacing:.3px;text-transform:uppercase}
.hero-box{position:absolute;left:235px;top:148px;width:345px;height:295px}
.hero-title{position:absolute;left:30px;top:14px;width:360px;font-weight:700;font-size:32px;line-height:1.15;color:var(--white);letter-spacing:.4px;text-transform:uppercase}
.hero-copy{position:absolute;left:29px;top:109px;width:290px;font-size:11px;line-height:15px;color:var(--white)}
.btn{display:inline-flex;align-items:center;justify-content:center;background:var(--blue);color:var(--white);font-weight:700;text-transform:uppercase;letter-spacing:.4px}
.hero-btn{position:absolute;left:29px;top:221px;width:136px;height:34px;font-size:12px;gap:6px}
.pager{position:absolute;top:467px;left:235px;display:flex;gap:8px;align-items:center}
.pager span{width:30px;height:30px;display:flex;align-items:center;justify-content:center;font-size:12px;font-weight:700;background:rgba(255,255,255,.25);color:var(--white)}
.pager span.on{background:var(--white);color:var(--blue)}
.pager .step{background:none;width:auto;font-size:9px;gap:6px;margin-left:20px}

/* headings */
.section-head{position:absolute;left:0;width:1200px;text-align:center;font-weight:700;font-size:26px;color:var(--ink);text-transform:uppercase;letter-spacing:.3px}
.section-head em{font-style:normal;color:var(--blue)}
.divider{position:absolute;left:458px;width:286px;height:14px}
.divider::before,.divider::after{content:"";position:absolute;top:7px;width:120px;height:1px;background:var(--line)}
.divider::before{left:0}.divider::after{right:0}
.divider i{position:absolute;left:136px;top:0;width:14px;height:14px;border:2px solid var(--blue)}

/* about */
.about{top:610px;height:406px;background:var(--grey-bg)}
.ghost{position:absolute;left:265px;top:20px;font-weight:800;font-family:"Montserrat",sans-serif;font-size:118px;color:#fbfbfb;letter-spacing:4px}
.about h2{position:absolute;left:235px;top:88px;font-size:19px;font-weight:700;color:var(--ink)}
.about p{position:absolute;left:235px;width:375px;font-size:11px;line-height:18.7px;color:#333}
.about-btn{position:absolute;left:235px;top:298px;width:107px;height:32px;font-size:8.5px}
.about-frame{position:absolute;left:635px;top:105px;width:312px;height:240px;border:1px solid #d2d4d8}
.about-photo{position:absolute;left:653px;top:92px;width:312px;height:238px;background:linear-gradient(180deg,#4a5066 0%,#3c4256 55%,#15161b 100%)}

/* services */
.services{top:1016px;height:466px;background:var(--white)}
.svc-col{position:absolute;top:0;width:232px;text-align:center}
.hex{position:absolute;top:154px;left:77px;width:78px;height:82px}
.svc-col h3{position:absolute;top:257px;left:-20px;width:272px;font-size:18px;font-weight:600;color:var(--ink)}
.svc-col p{position:absolute;top:288px;left:0;width:232px;font-size:10.6px;line-height:15px;color:#666}
.svc-btn{position:absolute;top:382px;left:62px;width:107px;height:28px;font-size:11px}

/* projects */
.projects{top:1482px;height:571px;background:var(--grey-bg)}
.panel{position:absolute;top:166px;width:300px;height:405px}
.panel .fill{position:absolute;inset:0}
.panel h4{position:absolute;left:25px;top:30px;font-size:17.5px;font-weight:600;color:var(--white);letter-spacing:.5px;text-transform:uppercase}
.panel h5{position:absolute;left:26px;top:56px;font-size:7px;font-weight:700;color:rgba(255,255,255,.8);letter-spacing:.3px;text-transform:uppercase}
.panel .vert{position:absolute;left:24px;top:348px;transform:rotate(-90deg);transform-origin:0 0;font-size:9px;letter-spacing:1.5px;color:rgba(255,255,255,.55);font-weight:700;text-transform:uppercase;white-space:nowrap}
.panel .nav-arrow{position:absolute;top:201px;font-size:9px;font-weight:700;color:var(--white);display:flex;gap:8px;align-items:center}

/* news */
.news{top:2053px;height:557px;background:var(--white)}
.card{position:absolute;top:157px;width:230px}
.card .img{height:152px}
.card .date{position:relative;margin:-15px 22px 0;height:33px;background:var(--white);text-align:center;font-size:11px;font-weight:600;color:var(--blue);line-height:33px}
.card h6{margin-top:14px;text-align:center;font-size:10px;font-weight:700;color:#222;line-height:15px}
.card p{margin-top:8px;text-align:center;font-size:8.5px;line-height:14.5px;color:#777}
.news-btn{position:absolute;left:525px;top:460px;width:152px;height:38px;font-size:9px}

/* partners */
.partners{top:2610px;height:268px;background:var(--grey-bg)}
.circ-arrow{position:absolute;top:174px;width:24px;height:24px;border:1px solid #555;border-radius:50%}

/* footer */
.footer{top:2878px;height:363px;background:var(--footer)}
.footer-glow{position:absolute;inset:0;background:linear-gradient(180deg,rgba(60,58,45,.35),rgba(27,28,34,0) 60%)}
.footer h2{position:absolute;left:235px;top:58px;font-family:"Montserrat",sans-serif;font-weight:800;font-size:24px;color:var(--white);letter-spacing:.5px}
.field{position:absolute;background:#2c2e36;border:1px solid #3a3d46;font-size:7.5px;color:#8d909a;padding:6px 8px}
.submit{position:absolute;left:878px;top:113px;width:88px;height:26px;font-size:8px}
.foot-brand{position:absolute;left:245px;top:204px;width:110px;text-align:center;color:var(--white);font-weight:600;font-size:13px;line-height:1.15;text-transform:uppercase}
.foot-brand small{display:block;font-size:7px;letter-spacing:1.5px}
.social{position:absolute;top:276px;left:252px;display:flex;gap:9px}
.social i{width:10px;height:10px;border-radius:50%;background:#5b5e68}
.foot-col{position:absolute;top:204px;font-size:7px;color:#c9cbd2;line-height:16px;text-transform:uppercase}
.foot-col b{display:block;color:var(--white);font-size:7.5px;margin-bottom:5px}
.contact-col{text-transform:none}
.contact-col div{display:flex;gap:8px;align-items:flex-start}
.contact-col svg{flex:none;margin-top:3px}
.copy{position:absolute;left:0;top:332px;width:1200px;text-align:center;font-size:7px;color:#a9acb5}
</style>
</head>
<body>

<section class="hero">
  <div class="hero-photo" role="img" aria-label="Aerial photo of an excavator grading a channel beside homes and trees"></div>
  <div class="brand"><span class="brand-mark"></span><div class="brand-name">Harlow Stonefield<small>Civil Construction</small></div></div>
  <nav class="nav"><span>Home</span><span>Project Gallery</span><span>Employment Application</span><span>Contact Us</span></nav>
  <div class="hero-box">
    <svg class="abs" style="left:0;top:0" width="345" height="295" viewBox="0 0 345 295">
      <path d="M345 2 H2 V293 H300 L345 250 V95" fill="none" stroke="#fff" stroke-width="3"/>
      <path d="M345 2 V10" stroke="#fff" stroke-width="3"/>
      <polygon points="345,252 345,295 302,295" fill="#3a52a8"/>
    </svg>
    <h1 class="hero-title">Harlow Stonefield Civil Construction</h1>
    <p class="hero-copy">Lorem ipsum dolor sit amet, consectetur adipiscing elit. Donec ut finibus enim. Donec sollicitudin turpis justo, sit amet porttitor lorem dictum sit amet. Integer vel tincidunt purus. Aliquam maximus lacus nec lorem accumsan blandit. Mauris eleifend, eros et mollis commodo, nisl metus finibus nibh, ac tempus dolor ipsum eu felis.</p>
    <span class="btn hero-btn">Learn More
      <svg width="14" height="10" viewBox="0 0 14 10"><path d="M0 5H12M8 1L12 5L8 9" fill="none" stroke="#fff" stroke-width="1.3"/></svg></span>
  </div>
  <div class="pager">
    <span class="on">1</span><span>2</span><span>3</span>
    <span class="step"><svg width="16" height="10" viewBox="0 0 16 10"><path d="M16 5H2M6 1L2 5L6 9" fill="none" stroke="#fff" stroke-width="1.2"/></svg>PREV</span>
    <span class="step" style="margin-left:6px">NEXT<svg width="16" height="10" viewBox="0 0 16 10"><path d="M0 5H14M10 1L14 5L10 9" fill="none" stroke="#fff" stroke-width="1.2"/></svg></span>
  </div>
  <svg class="abs" style="left:0;top:530px" width="1200" height="90" viewBox="0 0 1200 90">
    <polygon points="0,10 600,64 1200,10 1200,26 600,80 0,26" fill="#3a52a8"/>
    <polygon points="0,26 600,80 1200,26 1200,90 0,90" fill="#f2f2f2"/>
  </svg>
</section>

<section class="about">
  <div class="ghost">ABOUT US</div>
  <h2>ABOUT US</h2>
  <p style="top:126px">Lorem ipsum dolor sit amet, consectetur adipiscing elit. Donec ut finibus enim. Donec sollicitudin turpis justo, sit amet porttitor lorem dictum sit amet. Integer vel tincidunt purus. Aliquam maximus lacus nec lorem accumsan blandit. Mauris eleifend, eros et mollis commodo, nisl metus finibus nibh, ac tempus dolor ipsum eu felis.</p>
  <p style="top:238px">Morbi lacus enim, blandit quis interdum eu, rutrum vel massa. Suspendisse mollis mattis faucibus. Nunc luctus sem quis vehicula iaculis.</p>
  <span class="btn about-btn">Read More</span>
  <div class="about-frame"></div>
  <div class="about-photo" role="img" aria-label="Dusk silhouette of an excavator and heavy machinery on a job site"></div>
</section>

<section class="services">
  <svg class="abs" style="left:0;top:0" width="1200" height="466" viewBox="0 0 1200 466">
    <defs>
      <linearGradient id="svcLeft" x1="0" y1="0" x2="1" y2="1"><stop offset="0" stop-color="#5069b8"/><stop offset="1" stop-color="#2f4596"/></linearGradient>
      <linearGradient id="svcRight" x1="0" y1="0" x2="1" y2="1"><stop offset="0" stop-color="#9a9a9a"/><stop offset="1" stop-color="#2a2a2a"/></linearGradient>
    </defs>
    <polygon points="0,0 314,0 0,315" fill="url(#svcLeft)" role="img" aria-label="Blue-tinted photo of a long-reach excavator"/>
    <polygon points="1200,264 1200,466 994,466" fill="url(#svcRight)" role="img" aria-label="Black and white photo of an excavator at work"/>
  </svg>
  <div class="section-head" style="top:61px">Our <em>Services</em></div>
  <div class="divider" style="top:105px"><i></i></div>

  <div class="svc-col" style="left:234px">
    <svg class="hex" viewBox="0 0 78 82"><polygon points="39,1 76,21 76,61 39,81 2,61 2,21" fill="#fff" stroke="#d8d8d8" stroke-width="2"/><polygon points="39,8 70,25 70,57 39,74 8,57 8,25" fill="#8d8d8d"/></svg>
    <h3>Channel Stabilization</h3>
    <p>Lorem ipsum dolor sit amet, consectetur adipiscing elit. Donec ut finibus enim. Donec sollicitudin turpis justo, sit amet porttitor lorem dictum sit amet. Integer vel tincidunt purus. Aliquam maximus lacus nec lorem accumsan blandit.</p>
    <span class="btn svc-btn">Read More</span>
  </div>
  <div class="svc-col" style="left:485px">
    <svg class="hex" viewBox="0 0 78 82"><polygon points="39,1 76,21 76,61 39,81 2,61 2,21" fill="#fff" stroke="#d8d8d8" stroke-width="2"/><polygon points="39,8 70,25 70,57 39,74 8,57 8,25" fill="#8d8d8d"/></svg>
    <h3>Excavation and Grading</h3>
    <p>Lorem ipsum dolor sit amet, consectetur adipiscing elit. Donec ut finibus enim. Donec sollicitudin turpis justo, sit amet porttitor lorem dictum sit amet. Integer vel tincidunt purus. Aliquam maximus lacus nec lorem accumsan blandit.</p>
    <span class="btn svc-btn">Read More</span>
  </div>
  <div class="svc-col" style="left:736px">
    <svg class="hex" viewBox="0 0 78 82"><polygon points="39,1 76,21 76,61 39,81 2,61 2,21" fill="#fff" stroke="#d8d8d8" stroke-width="2"/><polygon points="39,8 70,25 70,57 39,74 8,57 8,25" fill="#8d8d8d"/></svg>
    <h3>Underground Utilities</h3>
    <p>Lorem ipsum dolor sit amet, consectetur adipiscing elit. Donec ut finibus enim. Donec sollicitudin turpis justo, sit amet porttitor lorem dictum sit amet. Integer vel tincidunt purus. Aliquam maximus lacus nec lorem accumsan blandit.</p>
    <span class="btn svc-btn">Read More</span>
  </div>
</section>

<section class="projects">
  <div class="section-head" style="top:58px">Our <em>Projects</em></div>
  <div class="divider" style="top:104px"><i></i></div>

  <div class="panel" style="left:0">
    <div class="fill" style="background:linear-gradient(180deg,#5a70bd,#4960ae 60%,#6172b0)" role="img" aria-label="Blue-tinted photo of a concrete pipe trench"></div>
    <h4>Underground Utilities</h4><h5>Harlow Stonefield Civil Construction</h5>
    <span class="vert">Harlow Stonefield Civil Construction</span>
    <span class="nav-arrow" style="left:76px"><svg width="16" height="10" viewBox="0 0 16 10"><path d="M16 5H2M6 1L2 5L6 9" fill="none" stroke="#fff" stroke-width="1.2"/></svg>PREV</span>
  </div>
  <div class="panel" style="left:300px">
    <div class="fill" style="background:linear-gradient(180deg,#8b93a3,#7d8696 60%,#8e95a2)" role="img" aria-label="Grey-tinted aerial photo of a road and drainage channel"></div>
    <h4>Channel Stabilization</h4><h5>Harlow Stonefield Civil Construction</h5>
    <span class="vert">Harlow Stonefield Civil Construction</span>
  </div>
  <div class="panel" style="left:600px">
    <div class="fill" style="background:linear-gradient(180deg,#4159b0,#3d55ab 60%,#4a5ea8)" role="img" aria-label="Blue-tinted photo of an excavator with palm trees"></div>
    <h4>Excavation and Grading</h4><h5>Harlow Stonefield Civil Construction</h5>
    <span class="vert">Harlow Stonefield Civil Construction</span>
  </div>
  <div class="panel" style="left:900px">
    <div class="fill" style="background:linear-gradient(180deg,#8f96a4,#858d9b 60%,#979ca6)" role="img" aria-label="Grey-tinted aerial photo of a new subdivision roundabout"></div>
    <h4>Land Development</h4><h5>Harlow Stonefield Civil Construction</h5>
    <span class="vert">Harlow Stonefield Civil Construction</span>
    <span class="nav-arrow" style="left:167px">NEXT<svg width="16" height="10" viewBox="0 0 16 10"><path d="M0 5H14M10 1L14 5L10 9" fill="none" stroke="#fff" stroke-width="1.2"/></svg></span>
  </div>
</section>

<section class="news">
  <div class="section-head" style="top:52px">Latest <em>News</em></div>
  <div class="divider" style="top:97px"><i></i></div>

  <div class="card" style="left:235px">
    <div class="img" style="background:linear-gradient(180deg,#6f8fb0,#4f6a5c 45%,#5d6a72)" role="img" aria-label="Photo of a stabilized creek channel with rock banks"></div>
    <div class="date">Jun 10, 2019</div>
    <h6>Morbi vel nisl purus. In varius dignissim<br>ligula quis accumsan quam</h6>
    <p>Lorem ipsum dolor sit amet, consectetur adipiscing<br>elit. Donec ut finibus enim. Donec sollicitudin turpis<br>justo, sit amet porttitor lorem dictum sit amet.</p>
  </div>
  <div class="card" style="left:486px">
    <div class="img" style="background:linear-gradient(180deg,#8aa0a8,#3f6a4a 40%,#3fa38a)" role="img" aria-label="Photo of a freshly hydroseeded green slope among trees"></div>
    <div class="date">May 27, 2019</div>
    <h6>Morbi vel nisl purus. In varius dignissim<br>ligula quis accumsan quam</h6>
    <p>Lorem ipsum dolor sit amet, consectetur adipiscing<br>elit. Donec ut finibus enim. Donec sollicitudin turpis<br>justo, sit amet porttitor lorem dictum sit amet.</p>
  </div>
  <div class="card" style="left:736px">
    <div class="img" style="background:linear-gradient(180deg,#8a7a5e,#b59430 45%,#8c7a40)" role="img" aria-label="Photo of a worker in a yellow trench box"></div>
    <div class="date">May 20, 2019</div>
    <h6>Morbi vel nisl purus. In varius dignissim<br>ligula quis accumsan quam</h6>
    <p>Lorem ipsum dolor sit amet, consectetur adipiscing<br>elit. Donec ut finibus enim. Donec sollicitudin turpis<br>justo, sit amet porttitor lorem dictum sit amet.</p>
  </div>
  <span class="btn news-btn">View More Blog</span>
</section>

<section class="partners">
  <div class="section-head" style="top:44px">Our <em>Partners</em></div>
  <div class="divider" style="top:91px"><i></i></div>
  <span class="circ-arrow" style="left:196px"><svg width="22" height="22" viewBox="0 0 22 22"><path d="M15 11H7M10 8L7 11L10 14" fill="none" stroke="#444" stroke-width="1"/></svg></span>
  <svg class="abs" style="left:250px;top:155px" width="710" height="70" viewBox="0 0 710 70">
    <rect x="8" y="16" width="130" height="34" rx="4" fill="#c8cace"/>
    <polygon points="232,5 254,17 254,41 232,53 210,41 210,17" fill="#b9bcc2"/>
    <circle cx="368" cy="33" r="20" fill="#b9bcc2"/>
    <circle cx="528" cy="28" r="20" fill="#9fa3aa"/>
    <polygon points="653,6 675,28 653,50 631,28" fill="#c4c6cb"/>
  </svg>
  <span class="circ-arrow" style="left:982px"><svg width="22" height="22" viewBox="0 0 22 22"><path d="M7 11H15M12 8L15 11L12 14" fill="none" stroke="#444" stroke-width="1"/></svg></span>
</section>

<section class="footer">
  <div class="footer-glow" role="img" aria-label="Dark photo of machinery on a job site"></div>
  <svg class="abs" style="left:0;top:0" width="1200" height="363" viewBox="0 0 1200 363">
    <defs><linearGradient id="ftBlue" x1="0" y1="1" x2="1" y2="0"><stop offset="0" stop-color="#2c3f8c" stop-opacity=".2"/><stop offset="1" stop-color="#3a52a8" stop-opacity=".85"/></linearGradient></defs>
    <polygon points="1200,40 1200,363 880,363" fill="url(#ftBlue)"/>
  </svg>
  <h2>CONTACT US</h2>
  <div class="field" style="left:467px;top:43px;width:143px;height:24px">First Name</div>
  <div class="field" style="left:618px;top:43px;width:143px;height:24px">Last Name</div>
  <div class="field" style="left:467px;top:78px;width:143px;height:24px">Phone</div>
  <div class="field" style="left:618px;top:78px;width:143px;height:24px">Email</div>
  <div class="field" style="left:769px;top:43px;width:197px;height:59px">Message</div>
  <span class="btn submit">Submit Now!</span>

  <div class="foot-brand">Harlow<br>Stonefield<small>Civil Construction</small></div>
  <div class="social"><i></i><i></i><i></i><i></i></div>

  <div class="foot-col" style="left:416px"><b>Quick Links</b>Home<br>About Us<br>Gallery<br>Contact Us</div>
  <div class="foot-col" style="left:532px"><b>Services</b>Channel Stabilization<br>Underground Utilities<br>Excavation and Grading<br>Land Development</div>
  <div class="foot-col" style="left:694px"><b>Explore Us</b>Support<br>FAQ<br>Client Feedback<br>Privacy Policy</div>
  <div class="foot-col contact-col" style="left:809px"><b>CONTACT INFO</b>
    <div><svg width="8" height="10" viewBox="0 0 8 10"><path d="M4 0C1.8 0 0 1.7 0 3.8C0 6.6 4 10 4 10S8 6.6 8 3.8C8 1.7 6.2 0 4 0Z" fill="#5b74c9"/></svg><span>14280 Lorem ipsum dolor sit amet,<br>consectetur adipiscing elit.</span></div>
    <div><svg width="8" height="9" viewBox="0 0 8 9"><path d="M1 0L3 2L2 3.5C2.8 5 3.8 6 5 6.8L6.3 5.8L8 7.8L6.8 9C3 8.2 0 5 0 1.2Z" fill="#5b74c9"/></svg><span>(600) 123 456 7890</span></div>
    <div><svg width="9" height="8" viewBox="0 0 9 8"><rect x="0" y="2" width="9" height="6" fill="#5b74c9"/><rect x="2" y="0" width="5" height="3" fill="#5b74c9"/></svg><span>(600) 123 456 7891</span></div>
    <div><svg width="9" height="7" viewBox="0 0 9 7"><rect width="9" height="7" fill="#5b74c9"/><path d="M0 0L4.5 4L9 0" fill="none" stroke="#1b1c22" stroke-width=".8"/></svg><span>info@harlowstonefieldcivil.com</span></div>
  </div>
  <div class="copy">Copyright © 2019 Harlow Stonefield Civil Construction. All rights reserved.</div>
</section>

</body>
</html>
```